High-End audio shop owner needs a business card

I need a personal Business Card for my Audio shop which exists since 1962. We offer high Quality brands, professional Attention and run our own repair-service-department. I look for a design which will be printed on high Quality paper and shall convey trust to the Client that we are very serious. Language is german.

```html
<!DOCTYPE html>
<html lang="de">
<head>
<meta charset="utf-8">
<title>Hi-Fi Lindenhof – Visitenkarte</title>
<link href="https://fonts.googleapis.com/css2?family=Lato:wght@400;700;900&display=swap" rel="stylesheet">
<style>
  :root {
    --stage: #2b2b2c;
    --card: #1e1f21;
    --card-back: #1c1d1f;
    --orange: #f26b12;
    --white: #f2f2f2;
    --rule: #6a6a6c;
    --texture-top: #25262a;
  }
  * { margin: 0; padding: 0; box-sizing: border-box; }
  html, body {
    width: 1200px; height: 1108px; overflow: hidden;
    background: var(--stage);
    font-family: "Lato", sans-serif;
  }
  .stage {
    position: relative; width: 1200px; height: 1108px;
    display: flex; justify-content: center; align-items: center; gap: 60px;
  }
  .card {
    position: relative; width: 420px; height: 690px;
    border-radius: 22px; overflow: hidden;
    box-shadow: 0 18px 40px rgba(0,0,0,.45);
  }
  .card--front { background: var(--card); }
  .card--back { background: var(--card-back); }

  .wordmark {
    font-family: "Lato", sans-serif; font-weight: 900;
    color: var(--orange); white-space: nowrap; letter-spacing: .5px;
  }
  .card--front .wordmark {
    position: absolute; top: 170px; left: 0; width: 100%;
    text-align: center; font-size: 40px;
  }

  .person {
    position: absolute; top: 380px; left: 0; width: 100%; text-align: center;
  }
  .person__name {
    color: var(--orange); font-size: 30px; font-weight: 400; letter-spacing: .5px;
  }
  .person__role { color: var(--white); font-size: 18px; margin-top: 2px; }

  .icon-row {
    position: absolute; top: 455px; left: 60px; width: 300px;
    display: flex; align-items: center; gap: 8px;
  }
  .icon-row .line { flex: 1; height: 1px; background: var(--rule); }
  .icon-row svg { width: 28px; height: 28px; display: block; }

  .contact {
    position: absolute; top: 500px; left: 0; width: 100%;
    text-align: center; color: var(--white); font-size: 19px; line-height: 1.35;
  }
  .divider {
    position: absolute; top: 590px; left: 90px; width: 240px;
    height: 1px; background: var(--rule);
  }
  .address {
    position: absolute; top: 605px; left: 0; width: 100%;
    text-align: center; color: var(--white); font-size: 19px; line-height: 1.35;
  }

  .back-texture {
    position: absolute; left: 0; top: 0; width: 100%; height: 560px;
    background: linear-gradient(to bottom, var(--texture-top), var(--card-back));
  }
  .card--back .wordmark {
    position: absolute; right: 40px; bottom: 90px; font-size: 24px;
  }
</style>
</head>
<body>
<main class="stage">
  <section class="card card--front" aria-label="Vorderseite">
    <div class="wordmark">Hi-Fi Lindenhof</div>

    <div class="person">
      <div class="person__name">LUKAS BERGER</div>
      <div class="person__role">Managing Director</div>
    </div>

    <div class="icon-row">
      <span class="line"></span>
      <svg viewBox="0 0 28 28" aria-label="Telefon" role="img">
        <circle cx="14" cy="14" r="13" fill="var(--orange)"/>
        <path d="M9 9c0 6 4 10 10 10l1.5-2.5-3-2-1.5 1.2c-1.8-.8-3-2-3.8-3.8L13.4 10l-2-3z" fill="#1e1f21"/>
      </svg>
      <svg viewBox="0 0 28 28" aria-label="E-Mail" role="img">
        <circle cx="14" cy="14" r="13" fill="var(--orange)"/>
        <rect x="7.5" y="9.5" width="13" height="9" fill="none" stroke="#1e1f21" stroke-width="1.6"/>
        <path d="M7.5 9.5l6.5 5 6.5-5" fill="none" stroke="#1e1f21" stroke-width="1.6"/>
      </svg>
      <svg viewBox="0 0 28 28" aria-label="Web" role="img">
        <circle cx="14" cy="14" r="13" fill="var(--orange)"/>
        <circle cx="14" cy="14" r="6.5" fill="none" stroke="#1e1f21" stroke-width="1.6"/>
        <ellipse cx="14" cy="14" rx="2.8" ry="6.5" fill="none" stroke="#1e1f21" stroke-width="1.4"/>
        <path d="M7.5 14h13" stroke="#1e1f21" stroke-width="1.4"/>
      </svg>
      <span class="line"></span>
    </div>

    <div class="contact">
      089-246 813 570<br>
      kontakt@lindenhof-audio.de<br>
      www.lindenhof-audio.de
    </div>
    <div class="divider"></div>
    <div class="address">
      Kastanienweg 17,<br>
      80995 München
    </div>
  </section>

  <section class="card card--back" aria-label="Rückseite">
    <div class="back-texture" role="img" aria-label="Dezentes Muster aus wiederholtem Firmenzeichen"></div>
    <div class="wordmark">Hi-Fi Lindenhof</div>
  </section>
</main>
</body>
</html>
```